Minimalist theatrical poster for the film

Create a poster, using some of the attached images for inspiration. Please match the font of the teaser poster for the title (The Bluewater) and leave space at the bottom for the credits block, which I will add later. Any characters presented on the poster should resemble the actors in the film, and not be clip art. The movie is about Owen, a 14 year old in the summer of 2001, and his first love (Greta). As he falls for her, he lets himself still be distracted by his good friend Maisie, eventually causing trouble in his relationships with Greta, Maisie, and best friend Theo. Trailer is included in the files below! Extra credit for a good marketing tag along the lines of "remember your first love" or something about the film being a romantic comedy adventure etc.

```html
<!DOCTYPE html>
<html lang="en">
<head>
<meta charset="utf-8">
<title>Owen &amp; The Bluewater — Poster</title>
<link href="https://fonts.googleapis.com/css2?family=Kaushan+Script&family=Big+Shoulders+Display:wght@200&display=swap" rel="stylesheet">
<style>
  :root {
    --ink: #1d1b3f;
    --paper-light: #fbe9d8;
    --paper-mid: #efcdb6;
    --paper-edge: #c99a86;
    --paper-deep: #a87466;
    --hair: #2e2534;
    --hair-soft: #5a4658;
    --skin: #d7b0b6;
    --shirt: #8fa6b3;
  }
  html, body {
    margin: 0;
    padding: 0;
    width: 800px;
    height: 1200px;
    overflow: hidden;
    background: var(--paper-mid);
  }
  .poster {
    position: relative;
    width: 800px;
    height: 1200px;
    overflow: hidden;
    background:
      radial-gradient(ellipse 420px 520px at 22% 38%, rgba(255,248,236,0.95) 0%, rgba(255,244,230,0.5) 45%, rgba(255,240,225,0) 75%),
      radial-gradient(ellipse 500px 700px at 50% 70%, rgba(245,214,196,0.6) 0%, rgba(245,214,196,0) 70%),
      linear-gradient(90deg, var(--paper-edge) 0%, var(--paper-mid) 12%, var(--paper-light) 40%, var(--paper-mid) 80%, var(--paper-deep) 100%);
  }
  .poster::after {
    content: "";
    position: absolute;
    inset: 0;
    background: linear-gradient(180deg, rgba(168,116,102,0.45) 0%, rgba(168,116,102,0) 14%, rgba(168,116,102,0) 85%, rgba(190,140,125,0.35) 100%);
    pointer-events: none;
  }
  .title {
    position: absolute;
    left: 0;
    top: 0;
    width: 800px;
    height: 520px;
    font-family: "Kaushan Script", cursive;
    fill: var(--ink);
  }
  .tagline {
    position: absolute;
    left: 0;
    top: 440px;
    width: 800px;
    height: 160px;
    font-family: "Big Shoulders Display", sans-serif;
    font-weight: 200;
    font-size: 64px;
    fill: var(--ink);
  }
  .still {
    position: absolute;
    left: 118px;
    top: 592px;
    width: 492px;
    height: 290px;
  }
</style>
</head>
<body>
  <main class="poster">
    <svg class="title" viewBox="0 0 800 520" aria-label="Owen &amp; The Bluewater">
      <text class="title-name" x="84" y="212" font-size="170" textLength="376" lengthAdjust="spacingAndGlyphs">Owen</text>
      <text class="title-amp" x="304" y="286" font-size="70">&amp;</text>
      <text class="title-the" x="208" y="380" font-size="76" textLength="122" lengthAdjust="spacingAndGlyphs">The</text>
      <text class="title-film" x="344" y="448" font-size="150" textLength="376" lengthAdjust="spacingAndGlyphs">Bluewater</text>
    </svg>

    <svg class="tagline" viewBox="0 440 800 160" aria-label="Remember your first love">
      <text x="164" y="512" textLength="356" lengthAdjust="spacing">REMEMBER YOUR</text>
      <text x="164" y="590" textLength="238" lengthAdjust="spacing">FIRST LOVE</text>
    </svg>

    <svg class="still" viewBox="0 0 492 290" role="img" aria-label="Painted film still: Owen leaning in to kiss Greta">
      <defs>
        <linearGradient id="still-fill" x1="0" y1="0" x2="0" y2="1">
          <stop offset="0%" stop-color="var(--hair)"/>
          <stop offset="38%" stop-color="var(--hair-soft)"/>
          <stop offset="62%" stop-color="var(--skin)"/>
          <stop offset="100%" stop-color="var(--shirt)"/>
        </linearGradient>
      </defs>
      <rect x="0" y="0" width="492" height="290" rx="24" fill="url(#still-fill)" opacity="0.9"/>
    </svg>
  </main>
</body>
</html>
```